Digital Marketing Consultant Needs a Business Card Design

I need a business card to brand myself - I'm a digital marketing consultant, and I do web design, SEO, lead generation, social media, etc. I'm overhauling my website (CorinneHalvorsk.com) and just had a snazzy new logo made.

I like the combo of yellow & gray - I find it eye-catching, upbeat and techie. The exact colors of yellow and gray that I like are #F6BF27 and #6D6D6D. But I'm open to suggestions and other color combinations!

I plan on printing the card using some high-end printing techniques that will ensure the card stands out - either really thick cards with colored edges, or spot UV. Not sure which yet, so if you want to incorporate that into your design, that'd be great!

I'm looking for a clean and modern design, but something that will really stand out when paired with 'fancy' printing.

Target Market(s)

Small and medium-sized business owners.

Industry/Entity Type

Printing

Contact Information for Business Card

Corinne Halvorsk
Digital Marketing
Call or Text: 850-555-0927
Corinne@CorinneHalvorsk.com
www.CorinneHalvorsk.com
@QPZ47 on Twitter

Font styles to use
Serif
Sans Serif

Requirements
Must have
• My logo, my contact information, and my "company colors" - #F6BF27 and #6D6D6D.
Nice to have
• If there's room to mention all the things that I do:
• Social Media, Web Design, SEO, Lead Generation, Conversion Funnels, PPC
• (don't add if it makes the card cluttered)

```html
<!DOCTYPE html>
<html lang="en">
<head>
<meta charset="utf-8">
<title>Corinne Halvorsk – Business Card</title>
<link rel="stylesheet" href="https://fonts.googleapis.com/css2?family=Cinzel:wght@400&family=Ubuntu:wght@300;400&family=Roboto+Condensed:wght@400&display=swap">
<style>
  :root {
    --slate: #566668;
    --sun: #f5bf03;
    --paper: #f7f8f8;
    --mist: #eef0f0;
    --brand-grey: #7d8d8b;
    --ink: #111111;
    --rule: #8fa0a0;
    --page: #ffffff;
  }
  html, body {
    margin: 0;
    padding: 0;
    width: 868px;
    height: 1200px;
    overflow: hidden;
    background: var(--page);
  }
  .sheet { display: block; width: 868px; height: 1200px; }
  .fill-slate { fill: var(--slate); }
  .fill-sun { fill: var(--sun); }
  .fill-paper { fill: var(--paper); }
  .edge-line { fill: none; stroke: var(--ink); stroke-width: 8; stroke-linejoin: miter; }
  .brand-square { fill: none; stroke: var(--brand-grey); stroke-width: 4; }
  .brand-name { font-family: "Cinzel", Georgia, serif; fill: var(--brand-grey); }
  .brand-tagline { font-family: "Ubuntu", Arial, sans-serif; font-weight: 300; fill: var(--brand-grey); letter-spacing: 3px; }
  .brand-rule { stroke: var(--rule); stroke-width: 1.5; }
  .contact-text { font-family: "Ubuntu", Arial, sans-serif; font-weight: 400; fill: var(--ink); font-size: 36px; }
  .contact-rule { stroke: #3d4a4c; stroke-width: 1.2; }
  .phone-number { font-family: "Roboto Condensed", "Arial Narrow", sans-serif; fill: var(--ink); font-size: 44px; }
  .icon { fill: var(--ink); }
  .icon-line { fill: none; stroke: var(--paper); stroke-width: 2; }
  .phone-tab { fill: var(--paper); }
</style>
</head>
<body>
<svg class="sheet" viewBox="0 0 1073 1484" preserveAspectRatio="none" xmlns="http://www.w3.org/2000/svg" role="group" aria-label="Business card, front and back">
  <defs>
    <radialGradient id="back-glow" cx="0.45" cy="0.45" r="0.75">
      <stop offset="0" stop-color="#ffffff"/>
      <stop offset="1" stop-color="#eceeee"/>
    </radialGradient>
  </defs>

  <!-- Front card -->
  <g class="card card-front">
    <rect class="fill-paper" x="0" y="0" width="1063" height="711"/>
    <path class="fill-slate" d="M0 0 H95 V68 Q95 110 53 110 H0 Z"/>
    <rect class="fill-slate" x="486" y="46" width="330" height="40" rx="12"/>
    <path class="fill-sun" d="M786 4 H1063 V114 H816 Q786 114 786 84 Z"/>

    <path class="fill-slate" d="M0 390 H40 L84 455 L125 390 H350 L395 328 H1063 V711 H0 Z"/>
    <polyline class="edge-line" points="0,390 40,390 84,455 125,390 350,390 395,328 1063,328"/>

    <rect class="fill-sun" x="0" y="652" width="1063" height="59"/>
    <polygon class="fill-slate" points="934,652 1002,652 968,688"/>
    <polygon class="fill-sun" points="966,594 986,622 946,622"/>

    <!-- Brand block -->
    <rect class="brand-square" x="264" y="73" width="94" height="93"/>
    <text class="brand-name" x="100" y="236" font-size="42" textLength="472" lengthAdjust="spacingAndGlyphs">CORINNE HALVORSK</text>
    <line class="brand-rule" x1="103" y1="262" x2="360" y2="262"/>
    <text class="brand-tagline" x="378" y="266" font-size="18">digital marketing</text>

    <!-- Contact details -->
    <g class="contact-web">
      <circle class="icon" cx="455" cy="420" r="30"/>
      <ellipse class="icon-line" cx="455" cy="420" rx="12" ry="28"/>
      <line class="icon-line" x1="427" y1="420" x2="483" y2="420"/>
      <text class="contact-text" x="496" y="424">www.CorinneHalvorsk.com</text>
      <line class="contact-rule" x1="496" y1="453" x2="955" y2="453"/>
    </g>
    <g class="contact-email">
      <rect class="icon" x="427" y="474" width="60" height="46"/>
      <polyline class="icon-line" points="429,477 457,501 485,477"/>
      <text class="contact-text" x="497" y="512">Corinne@CorinneHalvorsk.com</text>
      <line class="contact-rule" x1="497" y1="536" x2="667" y2="536"/>
    </g>
    <g class="contact-social">
      <rect class="icon" x="442" y="545" width="30" height="52" rx="4"/>
      <text class="contact-text" x="497" y="590">@QPZ47</text>
    </g>

    <g class="contact-phone">
      <path class="phone-tab" d="M50 711 V590 Q50 570 70 570 H109 V711 Z"/>
      <path class="icon" d="M92 590 L100 598 L92 606 Q84 618 88 636 L96 640 L92 652 L80 648 Q66 620 80 592 Z"/>
      <text class="phone-number" x="136" y="628" textLength="232" lengthAdjust="spacingAndGlyphs">850-555-0927</text>
    </g>
  </g>

  <!-- Back card -->
  <g class="card card-back">
    <rect x="10" y="773" width="1060" height="709" fill="url(#back-glow)"/>
    <path class="fill-slate" d="M887 773 H1070 V988 H937 Q887 988 887 938 Z"/>
    <path class="fill-sun" d="M625 828 H1070 V880 H625 Q615 880 615 870 V838 Q615 828 625 828 Z"/>

    <rect class="brand-square" x="443" y="1021" width="133" height="132" stroke-width="5"/>
    <text class="brand-name" x="210" y="1250" font-size="58" textLength="666" lengthAdjust="spacingAndGlyphs">CORINNE HALVORSK</text>
    <line class="brand-rule" x1="215" y1="1286" x2="578" y2="1286"/>
    <text class="brand-tagline" x="603" y="1292" font-size="25" textLength="266">digital marketing</text>
  </g>
</svg>
</body>
</html>
```